Graphic Design Project

Enhance the look of our home page. Please note, we do not want a complete redesign. We just want to tweak it some to optimize a user's first impression. Dev-ready files not required - a mockup will be fine (jpg or pdf).

I have attached source file for our current page.

Specific objectives:

- We really like the modern look of "www.lomifa.example" website. Would like to tighten up our appearance just a little to be more similar.

- A more creative design for the 4 text boxes in the middle of the page. Currently looks sub-par and outdated. We want a modern appearance.

- Colors can be revised some if you believe it will modernize / enhance the design.

Please submit your designs as soon as possible as we are under a huge time crunch and will be making our selections early.

The winner of this contest will get a followup project as well. We have a few upcoming tasks that will require a top-notch modern designer.

Industry/Entity Type

Graphic Design

Requirements
Must have
• - We really like the modern look of "www.lomifa.example" website. Would like to tighten up our appearance just a little to be more similar.

- A more creative design for the 4 text boxes in the middle of the page. Currently looks sub-par and outdated.

- Colors can be revised some if you believe it will enhance the appearance.

```html
<!DOCTYPE html>
<html lang="en">
<head>
<meta charset="utf-8">
<title>Reachgauge – The Source for Networking Superstars</title>
<link href="https://fonts.googleapis.com/css2?family=Archivo+Black&family=Arimo:wght@400;700&family=Oswald:wght@400&family=Playfair+Display:ital@1&display=swap" rel="stylesheet">
<style>
:root{
  --teal:#1a9cb7;
  --ink:#222;
  --hero-bg:#ececec;
  --band:#333333;
  --card:#e4e4e4;
  --card-stripe:#d9d9d9;
  --card-text:#3a3a3a;
  --green:#0fb553;
  --footer:#5b5b5b;
  --tab:#3a3a3a;
}
*{margin:0;padding:0;box-sizing:border-box}
html,body{width:1200px;height:840px;overflow:hidden;background:#fff;font-family:Arimo,Arial,sans-serif}
.page{position:relative;width:1200px;height:840px;overflow:hidden}

.site-header{position:absolute;left:0;top:0;width:1200px;height:86px;background:#fff;border-bottom:3px solid #2b2b2b;z-index:3}
.brand{position:absolute;left:200px;top:18px}
.brand-name{font-weight:700;font-size:33px;color:var(--teal);letter-spacing:-0.5px;line-height:1}
.brand-tagline{margin-top:8px;font-size:12px;color:#777;letter-spacing:0.6px;white-space:nowrap}
.account-nav{position:absolute;left:638px;top:16px;width:362px}
.account-nav-label{text-align:center;font-size:12px;font-weight:700;color:#666;margin-left:20px}
.account-btn{position:absolute;top:20px;height:31px;border-radius:4px;font-size:10px;font-weight:700;display:flex;align-items:center;justify-content:center;white-space:nowrap}
.account-btn.superstars{left:0;width:167px;background:#e3e3e3;border:2px solid #cfcfcf;color:var(--teal)}
.account-btn.business{left:195px;width:167px;background:var(--teal);color:#fff}
.account-divider{position:absolute;left:180px;top:18px;width:1px;height:35px;background:#ccc}

.hero{position:absolute;left:0;top:86px;width:1200px;height:716px;background:radial-gradient(ellipse at 55% 40%,#f4f4f4,var(--hero-bg) 70%)}
.hero-photo{position:absolute;left:690px;top:86px;width:405px;height:716px;background:linear-gradient(180deg,#c9a08a 0%,#b98c78 28%,#4a5275 45%,#3c4468 100%);border-radius:180px 180px 0 0;z-index:1}
.hero-copy{position:absolute;left:40px;top:238px;width:336px;text-align:right;z-index:2}
.hero-title{font-family:Oswald,'Arial Narrow',sans-serif;font-weight:400;font-size:42px;color:var(--ink);line-height:1;letter-spacing:-0.5px;white-space:nowrap}
.hero-sub{font-family:'Playfair Display',Georgia,serif;font-style:italic;font-size:29px;line-height:1.1;color:var(--ink);margin-top:4px;white-space:nowrap}
.signin-btn{position:absolute;left:202px;top:338px;width:152px;height:40px;background:var(--green);color:#fff;font-size:19px;display:flex;align-items:center;justify-content:center;gap:8px;box-shadow:0 2px 4px rgba(0,0,0,.2);z-index:2;letter-spacing:0.5px}
.signin-btn .dot{width:10px;height:10px;border-radius:50%;background:#fff}

.features{position:absolute;left:0;top:438px;width:1200px;height:272px;background:rgba(45,45,45,.96);z-index:2}
.feature-card{position:absolute;top:45px;width:253px;height:185px;padding:24px 6px 0 13px;background:repeating-linear-gradient(90deg,var(--card) 0 4px,var(--card-stripe) 4px 6px);box-shadow:0 0 0 1px #cfcfcf inset}
.feature-card h2{font-family:'Archivo Black','Arial Black',sans-serif;font-weight:400;font-size:30px;color:var(--teal);line-height:1;letter-spacing:0.3px}
.feature-card p{margin-top:17px;font-size:19.5px;line-height:26px;color:var(--card-text);white-space:nowrap}
.c1{left:26px}.c2{left:322px;padding-left:14px}.c3{left:619px;padding-left:17px}.c4{left:916px;padding-left:15px}

.follow-tab{position:absolute;top:772px;height:30px;background:var(--tab);color:#fff;font-size:10px;font-weight:700;display:flex;align-items:center;border-radius:4px 4px 0 0;z-index:2;white-space:nowrap}
.follow-tab .mark{width:25px;height:30px;border-right:1px solid #555;display:flex;align-items:center;justify-content:center}
.follow-tab .mark span{width:10px;height:10px;background:#fff}
.follow-tab .label{padding:0 8px}
.follow-tab.chirp{left:200px;width:145px}
.follow-tab.wall{left:358px;width:145px}

.site-footer{position:absolute;left:0;top:802px;width:1200px;height:38px;background:rgba(85,85,85,.95);color:#fff;z-index:2}
.copyright{position:absolute;left:202px;top:14px;font-size:9.5px;white-space:nowrap}
.social-dots{position:absolute;left:468px;top:11px;display:flex;gap:9px}
.social-dots span{width:16px;height:16px;border-radius:50%;background:#eee}
.footer-links{position:absolute;left:586px;top:0;display:flex;height:38px;list-style:none}
.footer-links li{font-size:13px;padding:0 13px;display:flex;align-items:center;border-left:1px solid #888;white-space:nowrap}
.footer-links li:first-child{border-left:none}
</style>
</head>
<body>
<div class="page">
  <header class="site-header">
    <div class="brand">
      <div class="brand-name">Reachgauge</div>
      <div class="brand-tagline">The Source for Networking Superstars</div>
    </div>
    <nav class="account-nav">
      <div class="account-nav-label">SIGN IN or LEARN MORE</div>
      <div class="account-btn superstars">NETWORKING SUPERSTARS</div>
      <div class="account-divider"></div>
      <div class="account-btn business">BUSINESS USERS/RECRUITERS</div>
    </nav>
  </header>

  <section class="hero"></section>
  <div class="hero-photo" role="img" aria-label="Photo of a smiling businesswoman in a pinstripe suit pointing toward the sign-in call to action"></div>
  <div class="hero-copy">
    <h1 class="hero-title">ACTIVATE PROFILE</h1>
    <div class="hero-sub">Instantly With Chirpline</div>
  </div>
  <div class="signin-btn"><span class="dot"></span>Sign In</div>

  <section class="features">
    <article class="feature-card c1"><h2>COMPARE</h2><p>against others within<br>our databse to see how<br>you rank</p></article>
    <article class="feature-card c2"><h2>PRINT</h2><p>to strengthen and<br>supplement your resume<br>by showcasing actual<br>results</p></article>
    <article class="feature-card c3"><h2>SHARE</h2><p>a link to your profile in<br>social activity... personal<br>branding at its best</p></article>
    <article class="feature-card c4"><h2>TRACK</h2><p>your profile traffic with<br>detailed statistic reporting</p></article>
  </section>

  <div class="follow-tab chirp"><div class="mark"><span></span></div><div class="label">Follow us on Chirpline</div></div>
  <div class="follow-tab wall"><div class="mark"><span></span></div><div class="label">Follow us on Friendwall</div></div>

  <footer class="site-footer">
    <div class="copyright">Copyright © 2013 Reachgauge. All rights reserved.</div>
    <div class="social-dots"><span></span><span></span><span></span><span></span></div>
    <ul class="footer-links">
      <li>Contact Us</li>
      <li>Sample Profile</li>
      <li>Terms of Services</li>
      <li>Privacy Policy</li>
    </ul>
  </footer>
</div>
</body>
</html>
```